Product Menu 8 x 11- Home Inspection Company Ancillary Services

Hello, on the front side of the flyer will be all about sewer camera inspections. These will include the images of the damages on the front and the information on the Sewer Scope Inspections: Safeguard Your Home from Hidden Plumbing Issues.
On the back will include indoor air quality. Solar Panel Inspections, Roof Certifications, and Expert Raised Foundation Review.
Please use logo and colors as a branding guide for the flyer.
$275- Sewer Camera Fee
$495 -Indoor Air Quality Inspection- Getting an indoor air quality (IAQ) inspection for mold when buying a home is crucial for health, safety, and financial protection. Mold can cause serious respiratory issues, especially for those with allergies or asthma, and toxic molds like black mold pose additional risks. It often grows in hidden areas, such as behind walls or in HVAC systems, often linked to water damage or structural issues. Early detection allows you to negotiate remediation costs, prevent mold from spreading, and avoid expensive repairs, ensuring a safe and sound investment.
$395 -Solar Panel Inspection- Getting a solar panel inspection when buying a home is essential to ensure efficiency, safety, and long-term savings. It verifies the system’s condition, identifying issues like damaged panels, faulty wiring, or inefficient inverters that could impact performance or pose safety risks. The inspection also evaluates the system’s energy output and compatibility with your energy needs, ensuring you’re benefiting from the investment. Additionally, understanding the age, warranty, and maintenance history of the system helps avoid unexpected repair costs and maximizes the value of this eco-friendly feature.
$399 Roof Certifications- Obtaining a roof certification when buying a home is vital for assessing the roof's condition, lifespan, and potential repair needs. This certification provides a professional evaluation, ensuring the roof is free from leaks, damage, or structural issues, which could lead to costly repairs. Many insurance companies require a roof certification before issuing or renewing a policy, particularly for older roofs, to confirm it meets safety standards. Having this certification not only provides peace of mind but also helps facilitate insurance coverage and protects your investment in the property.
$199- Advanced Foundation Review-An advanced foundation review by a licensed foundation contractor is essential when buying a home, as it provides a detailed assessment beyond what a general home inspector can offer. While home inspectors are trained generalists who identify visible issues, a foundation contractor is a specialist with the expertise to evaluate structural integrity, detect hidden problems, and determine the severity of any concerns. This specialized review can uncover issues like uneven settling, cracks, or drainage problems that may require repairs, ensuring you have a clear understanding of the foundation's condition before making a significant investment.
Real Estate Buyers and Real Estate Agents

```html
<!DOCTYPE html>
<html lang="en">
<head>
<meta charset="utf-8">
<title>Summit Crest – Ancillary Services Flyer</title>
<link href="https://fonts.googleapis.com/css2?family=Poppins:wght@400;500;600;700;800&display=swap" rel="stylesheet">
<style>
  :root{
    --brand-blue:#1b6fc6;
    --brand-navy:#0e1d3b;
    --brand-red:#e63b46;
    --tint:#eef5fc;
    --card:#f1f6fb;
    --ink:#2a3446;
    --paper:#ffffff;
    --backdrop:#d9dadc;
  }
  *{box-sizing:border-box;margin:0;padding:0}
  html,body{width:1200px;height:1117px;overflow:hidden}
  body{background:var(--backdrop);font-family:"Poppins",sans-serif;position:relative;color:var(--ink)}
  .sheet{position:absolute;top:196px;width:560px;height:725px;background:var(--paper);overflow:hidden;box-shadow:0 6px 18px rgba(0,0,0,.18)}
  .sheet--front{left:25px}
  .sheet--back{left:615px}

  /* FRONT */
  .brand{position:absolute;left:20px;top:30px;width:220px;text-align:center}
  .brand__dot{width:92px;height:92px;border-radius:50%;background:var(--brand-red);margin:0 auto 10px}
  .brand__name{font-weight:800;font-size:24px;color:var(--brand-blue);letter-spacing:.5px;line-height:1}
  .brand__tag{font-size:8.5px;font-weight:600;color:var(--brand-blue);letter-spacing:.8px;margin-top:5px;text-transform:uppercase}
  .hero-copy{position:absolute;left:250px;top:0;right:0;height:260px;background:var(--tint);padding:34px 18px 0 22px;text-align:center}
  .hero-copy__kicker{color:var(--brand-red);font-weight:600;font-size:14px;line-height:1.5}
  .hero-copy__title{color:var(--brand-blue);font-weight:700;font-size:27px;line-height:1.1;margin-top:6px}
  .explain{position:absolute;left:0;right:0;top:260px;height:210px;background:linear-gradient(180deg,#1c3463,var(--brand-navy))}
  .damage-shots{position:absolute;left:22px;right:22px;top:190px;display:flex;justify-content:space-between}
  .damage-shots__item{width:156px;height:156px;border-radius:50%;border:5px solid var(--paper);box-shadow:0 3px 8px rgba(0,0,0,.3)}
  .shot-roots{background:radial-gradient(circle at 45% 40%,#8a6a45,#4a3622)}
  .shot-crack{background:radial-gradient(circle at 50% 45%,#d8d6d0,#6e6b66)}
  .shot-rust{background:radial-gradient(circle at 50% 50%,#2a2418 15%,#7a6540 60%,#3b3020)}
  .explain__title{position:absolute;top:94px;left:0;right:0;text-align:center;color:#fff;font-weight:600;font-size:19px;line-height:1.3}
  .explain__text{position:absolute;top:124px;left:40px;right:40px;text-align:center;color:#eef2f8;font-size:12px;line-height:1.42}
  .reasons{position:absolute;left:0;top:470px;width:270px;padding:22px 0 0 28px}
  .reasons__title{color:var(--brand-blue);font-weight:700;font-size:15px;line-height:1.2}
  .reasons__list{list-style:none;margin-top:8px}
  .reasons__list li{display:flex;align-items:center;gap:8px;font-weight:600;font-size:13.5px;line-height:20px;color:var(--brand-navy);margin-bottom:2px}
  .reasons__list svg{width:13px;height:13px;flex:none}
  .inspector-photo{position:absolute;right:0;top:470px;width:310px;height:200px;background:linear-gradient(135deg,#8fa16a,#4d5a3a 55%,#2a3550);clip-path:polygon(18% 0,100% 0,100% 100%,0 100%)}
  .front-footer{position:absolute;left:0;right:0;bottom:0;height:55px;background:var(--brand-blue);color:#fff;font-weight:700;font-size:22px;display:flex;align-items:center;justify-content:center}

  /* BACK */
  .fee{position:absolute;left:0;top:0;width:560px;height:205px}
  .fee__panel{position:absolute;left:0;top:0;width:330px;height:205px;background:var(--brand-blue);clip-path:polygon(0 0,100% 0,75% 100%,0 100%)}
  .fee__photo{position:absolute;left:255px;top:0;right:0;height:205px;background:linear-gradient(160deg,#7d7264,#6f8a4e 60%,#b7a27b);clip-path:polygon(30% 0,100% 0,100% 100%,0 100%)}
  .fee__label{position:absolute;left:28px;top:28px;color:#fff;font-weight:700;font-size:27px;line-height:1.12}
  .fee__price{position:absolute;left:20px;top:108px;background:var(--brand-navy);color:#fff;font-weight:700;font-size:44px;padding:0 22px;line-height:64px;border-radius:6px}
  .services{position:absolute;left:22px;right:18px;top:215px}
  .service{display:flex;gap:12px;background:var(--card);border-radius:10px;padding:7px 10px 7px 7px;margin-bottom:9px;height:104px}
  .service__photo{width:110px;flex:none;border-radius:8px}
  .photo-air{background:linear-gradient(135deg,#4a5566,#1f2937)}
  .photo-solar{background:linear-gradient(160deg,#2a4d80,#c9b48e)}
  .photo-roof{background:linear-gradient(150deg,#3d5f92,#7d8a6a)}
  .photo-found{background:linear-gradient(150deg,#6b4c2f,#d7b98a)}
  .service__head{font-weight:600;font-size:12px;color:var(--brand-blue);margin-top:2px}
  .service__price{color:var(--brand-red);margin-right:6px}
  .service__text{font-size:6.9px;line-height:1.36;color:#3c4556;margin-top:3px}
  .back-footer{position:absolute;left:0;right:0;bottom:0;height:62px;background:var(--brand-red);color:#fff;display:flex;align-items:center;padding:0 22px;gap:14px}
  .back-footer__phone{display:flex;align-items:center;gap:6px;font-weight:700;font-size:22px;padding-right:14px;border-right:1px solid rgba(255,255,255,.7)}
  .back-footer__phone svg{width:16px;height:16px}
  .back-footer__links{font-size:8.5px;line-height:1.6}
  .back-footer__brand{margin-left:auto;text-align:center;display:flex;align-items:center;gap:6px}
  .back-footer__dot{width:26px;height:26px;border-radius:50%;background:#fff}
  .back-footer__name{font-weight:800;font-size:13px;color:#fff}
</style>
</head>
<body>

<section class="sheet sheet--front">
  <div class="hero-copy">
    <p class="hero-copy__kicker">The Sewer Scope Inspections:</p>
    <h1 class="hero-copy__title">Safeguard<br>Your Home from<br>Hidden Plumbing<br>Issues.</h1>
  </div>
  <div class="brand">
    <div class="brand__dot"></div>
    <div class="brand__name">SUMMIT CREST</div>
    <div class="brand__tag">Inspection Professionals</div>
  </div>

  <div class="explain">
    <h2 class="explain__title">What is a Sewer Scope Inspection?</h2>
    <p class="explain__text">A sewer scope inspection uses a camera to inspect your home's sewer lines. The camera is inserted into the sewer pipe, allowing an inspector to detect blockages, cracks, tree root intrusions, and other issues that can cause significant damage if left unaddressed.</p>
  </div>
  <div class="damage-shots">
    <div class="damage-shots__item shot-roots" role="img" aria-label="Sewer camera view of tree roots inside a pipe"></div>
    <div class="damage-shots__item shot-crack" role="img" aria-label="Sewer camera view of a crack in a pipe wall"></div>
    <div class="damage-shots__item shot-rust" role="img" aria-label="Sewer camera view of a corroded pipe interior"></div>
  </div>

  <div class="reasons">
    <h3 class="reasons__title">Why You Should Get a<br>Sewer Scope Inspection:</h3>
    <ul class="reasons__list">
      <li><svg viewBox="0 0 14 14"><circle cx="7" cy="7" r="7" fill="#e63b46"/><path d="M4 7.2l2 2 4-4.2" stroke="#fff" stroke-width="1.8" fill="none"/></svg>Prevent Costly Repairs,</li>
      <li><svg viewBox="0 0 14 14"><circle cx="7" cy="7" r="7" fill="#e63b46"/><path d="M4 7.2l2 2 4-4.2" stroke="#fff" stroke-width="1.8" fill="none"/></svg>Protect Your Investment</li>
      <li><svg viewBox="0 0 14 14"><circle cx="7" cy="7" r="7" fill="#e63b46"/><path d="M4 7.2l2 2 4-4.2" stroke="#fff" stroke-width="1.8" fill="none"/></svg>Catch Hidden Problems</li>
      <li><svg viewBox="0 0 14 14"><circle cx="7" cy="7" r="7" fill="#e63b46"/><path d="M4 7.2l2 2 4-4.2" stroke="#fff" stroke-width="1.8" fill="none"/></svg>Avoid Health Hazards</li>
      <li><svg viewBox="0 0 14 14"><circle cx="7" cy="7" r="7" fill="#e63b46"/><path d="M4 7.2l2 2 4-4.2" stroke="#fff" stroke-width="1.8" fill="none"/></svg>Ensure Proper Functioning</li>
    </ul>
  </div>
  <div class="inspector-photo" role="img" aria-label="Inspector on a ladder at a roof edge above a garden"></div>
  <div class="front-footer">www.summitcrestinspect.com</div>
</section>

<section class="sheet sheet--back">
  <div class="fee">
    <div class="fee__photo" role="img" aria-label="Inspector feeding a sewer camera into a cleanout beside a stone wall"></div>
    <div class="fee__panel"></div>
    <h1 class="fee__label">Sewer<br>Camera Fee</h1>
    <div class="fee__price">$275</div>
  </div>

  <div class="services">
    <article class="service">
      <div class="service__photo photo-air" role="img" aria-label="Inspector setting up an air quality sampler"></div>
      <div>
        <h3 class="service__head"><span class="service__price">$495</span>Indoor Air Quality Inspection</h3>
        <p class="service__text">Indoor Air Quality Inspection- Getting an indoor air quality (IAQ) inspection for mold when buying a home is crucial for health, safety, and financial protection. Mold can cause serious respiratory issues, especially for those with allergies or asthma, and toxic molds like black mold pose additional risks. It often grows in hidden areas, such as behind walls or in HVAC systems, often linked to water damage or structural issues. Early detection allows you to negotiate remediation costs, prevent mold from spreading, and avoid expensive repairs, ensuring a safe and sound investment.</p>
      </div>
    </article>
    <article class="service">
      <div class="service__photo photo-solar" role="img" aria-label="Home roof with solar panels"></div>
      <div>
        <h3 class="service__head"><span class="service__price">$395</span>Solar Panel Inspection</h3>
        <p class="service__text">Getting a solar panel inspection when buying a home is essential to ensure efficiency, safety, and long-term savings. It verifies the system's condition, identifying issues like damaged panels, faulty wiring, or inefficient inverters that could impact performance or pose safety risks. The inspection also evaluates the system's energy output and compatibility with your energy needs, ensuring you're benefiting from the investment. Additionally, understanding the age, warranty, and maintenance history of the system helps avoid unexpected repair costs and maximizes the value of this eco-friendly feature.</p>
      </div>
    </article>
    <article class="service">
      <div class="service__photo photo-roof" role="img" aria-label="Aerial view of a blue metal roof"></div>
      <div>
        <h3 class="service__head"><span class="service__price">$399</span>Roof Certifications</h3>
        <p class="service__text">Obtaining a roof certification when buying a home is vital for assessing the roof's condition, lifespan, and potential repair needs. This certification provides a professional evaluation, ensuring the roof is free from leaks, damage, or structural issues, which could lead to costly repairs. Many insurance companies require a roof certification before issuing or renewing a policy, particularly for older roofs, to confirm it meets safety standards. Having this certification not only provides peace of mind but also helps facilitate insurance coverage and protects your investment in the property.</p>
      </div>
    </article>
    <article class="service">
      <div class="service__photo photo-found" role="img" aria-label="Crawl space beneath a raised foundation"></div>
      <div>
        <h3 class="service__head"><span class="service__price">$199</span>Advanced Foundation Review</h3>
        <p class="service__text">An advanced foundation review by a licensed foundation contractor is essential when buying a home, as it provides a detailed assessment beyond what a general home inspector can offer. While home inspectors are trained generalists who identify visible issues, a foundation contractor is a specialist with the expertise to evaluate structural integrity, detect hidden problems, and determine the severity of any concerns. This specialized review can uncover issues like uneven settling, cracks, or drainage problems that may require repairs, ensuring you have a clear understanding of the foundation's condition before making a significant investment.</p>
      </div>
    </article>
  </div>

  <footer class="back-footer">
    <div class="back-footer__phone">
      <svg viewBox="0 0 24 24"><path fill="#fff" d="M6.6 10.8a15 15 0 006.6 6.6l2.2-2.2a1 1 0 011-.25 11.4 11.4 0 003.6.57 1 1 0 011 1V20a1 1 0 01-1 1A17 17 0 013 4a1 1 0 011-1h3.5a1 1 0 011 1c0 1.25.2 2.45.57 3.57a1 1 0 01-.25 1z"/></svg>
      800-555-0142
    </div>
    <div class="back-footer__links">
      <div>care@summitcrestinspect.com</div>
      <div>www.summitcrestinspect.com</div>
    </div>
    <div class="back-footer__brand">
      <div class="back-footer__dot"></div>
      <div class="back-footer__name">SUMMIT CREST</div>
    </div>
  </footer>
</section>

</body>
</html>
```